Classical Chamber Choir needs an electronic and printable flyer for an Easter Concert

I am the new Artistic Director of the Halvane Chorale. We would like to advertise our upcoming concert on April 5 and are seeking a new, more youthful, contemporary look for the choir's advertising. Previously they have used classical curly letters and dark colours. Perhaps black/grey and white would work?
The choir is 27 years old and has many loyal and some quite elderly singers. We would now like to extend our appeal to the younger singers who are in the choir - age group 35 - 60 and we are keen to attract more in the 30/40 age group. I would like something contemporary in feel, uncluttered, minimalist and artistically appealing. More Morwelt than Pilard - more Fenzarotti than Drecklin. Some inspiration starters: Valdurro line drawings, linocut designs, Emil Vortanek pencil drawings. I am hoping these references might inspire you. Here are some other ideas using line from Gyula Fenyvesi:
https://pics.vistrel.example/qw7RtPz2LmNbXcYhA
https://pics.vistrel.example/Hs3KdVn8WpJtRfZ4M
We would require an A4 flyer, (high res. and low res.) DL, jpg for Chatterly and a 10cm. size to put on the front of the Concert Programme.

```html
<!DOCTYPE html>
<html lang="en">
<head>
<meta charset="utf-8">
<title>Stenholt at Easter — Halvane Chorale</title>
<link rel="stylesheet" href="https://fonts.googleapis.com/css2?family=IM+Fell+English&family=IM+Fell+English+SC&family=Montserrat:wght@400;500;600&family=Old+Standard+TT:wght@400;700&display=swap">
<style>
  :root {
    --paper: #f1f1f1;
    --sketch-light: #f4f4f4;
    --sketch-mid: #d9d9d9;
    --ink: #111111;
    --ink-soft: #2a2a2a;
    --white: #ffffff;
  }
  * { margin: 0; padding: 0; box-sizing: border-box; }
  html, body { width: 943px; height: 1200px; overflow: hidden; background: var(--paper); }
  .flyer {
    position: relative;
    width: 943px;
    height: 1200px;
    background: var(--paper);
    color: var(--ink);
    font-family: "Montserrat", Arial, sans-serif;
  }
  .sketch-backdrop {
    position: absolute;
    inset: 12px;
    background:
      radial-gradient(ellipse at 70% 35%, var(--sketch-mid) 0%, transparent 55%),
      radial-gradient(ellipse at 15% 90%, #cfcfcf 0%, transparent 35%),
      linear-gradient(160deg, var(--sketch-light) 0%, #e2e2e2 50%, #dcdcdc 100%);
  }
  .centered { position: absolute; left: 0; right: 0; text-align: center; }
  .presenter { top: 34px; font-size: 19px; font-weight: 600; letter-spacing: 9px; }
  .title {
    font-family: "IM Fell English SC", "IM Fell English", Georgia, serif;
    font-size: 104px; line-height: 98px; top: 70px; color: var(--ink);
  }
  .title-rule { position: absolute; left: 131px; width: 712px; top: 268px; height: 3px; background: linear-gradient(90deg, transparent, var(--ink) 8%, var(--ink) 92%, transparent); }
  .work { top: 292px; font-size: 26px; font-weight: 600; letter-spacing: 5px; }
  .company { top: 325px; font-size: 17px; }
  .masters { top: 350px; font-size: 30px; font-weight: 500; letter-spacing: 5px; }
  .composers { top: 387px; font-size: 18px; font-weight: 500; }
  .frame { position: absolute; border: 2px solid var(--ink); border-radius: 8px; display: flex; align-items: center; justify-content: center; text-align: center; }
  .venue { left: 116px; top: 439px; width: 426px; height: 79px; flex-direction: column; align-items: flex-start; padding-left: 40px; }
  .venue-name { font-family: "Old Standard TT", Georgia, serif; font-size: 23px; line-height: 30px; }
  .venue-street { font-size: 20px; line-height: 28px; }
  .pin { position: absolute; left: -14px; top: 26px; width: 28px; height: 28px; background: var(--paper); }
  .date { left: 553px; top: 452px; width: 298px; height: 56px; font-family: "Old Standard TT", Georgia, serif; font-size: 28px; }
  .section-head { font-family: "Old Standard TT", Georgia, serif; font-weight: 700; font-size: 26px; }
  .name-box { width: 260px; height: 54px; font-size: 17px; background: transparent; }
  .director { top: 960px; font-size: 17px; }
  .director strong { font-family: "Old Standard TT", Georgia, serif; font-weight: 400; font-size: 33px; letter-spacing: 1px; }
  .tickets-label { position: absolute; left: 37px; top: 1032px; font-family: "Old Standard TT", Georgia, serif; font-size: 22px; }
  .price { position: absolute; top: 1026px; width: 120px; height: 44px; background: var(--ink); color: var(--white); border-radius: 9px; display: flex; align-items: center; justify-content: center; font-family: "Old Standard TT", Georgia, serif; font-size: 34px; }
  .free-box { position: absolute; left: 534px; top: 1004px; width: 384px; height: 84px; background: var(--ink); color: var(--white); border-radius: 10px; text-align: center; }
  .free-word { font-family: "IM Fell English", Georgia, serif; font-size: 50px; line-height: 54px; margin-top: 4px; }
  .free-note { font-size: 19px; font-weight: 500; }
  .programmes { top: 1117px; font-family: "Old Standard TT", Georgia, serif; font-size: 19px; }
  .donation { top: 1147px; font-size: 21px; font-weight: 600; letter-spacing: 9px; }
  .donation-rule { position: absolute; top: 1160px; height: 1.5px; width: 104px; background: var(--ink-soft); }
</style>
</head>
<body>
<main class="flyer">
  <div class="sketch-backdrop" role="img" aria-label="Soft grey pencil-line drawing filling the flyer background"></div>

  <p class="centered presenter">HALVANE CHORALE PRESENT</p>
  <h1 class="centered title">STENHOLT<br>AT EASTER</h1>
  <div class="title-rule"></div>

  <p class="centered work">STENHOLT STABAT MATER OP 38</p>
  <p class="centered company">in the company of the</p>
  <p class="centered masters">RUSSIAN MASTERS</p>
  <p class="centered composers">Verbitsov, Dravka, Rastovinov, Morozin</p>

  <div class="frame venue">
    <svg class="pin" viewBox="0 0 28 28" aria-hidden="true">
      <rect x="2" y="2" width="24" height="24" rx="5" fill="none" stroke="#111" stroke-width="2.5"/>
      <path d="M14 7a5 5 0 0 0-5 5c0 4 5 9 5 9s5-5 5-9a5 5 0 0 0-5-5z" fill="#111"/>
      <circle cx="14" cy="12" r="2" fill="#f1f1f1"/>
    </svg>
    <span class="venue-name">ST ANSELM'S CHURCH</span>
    <span class="venue-street">CORRIN STREET ASHGROVE HILL</span>
  </div>
  <div class="frame date">5PM APRIL 5 2020</div>

  <h2 class="centered section-head" style="top:537px">SOLOISTS</h2>
  <div class="frame name-box" style="left:68px;top:580px">LENA HARTWELL</div>
  <div class="frame name-box" style="left:346px;top:580px">ADRIAN COLBECK</div>
  <div class="frame name-box" style="left:626px;top:580px">GERALD MARWOOD</div>

  <h2 class="centered section-head" style="top:653px">MEN OF NOTE</h2>
  <div class="frame name-box" style="left:68px;top:696px">STRING QUARTET</div>
  <div class="frame name-box" style="left:346px;top:696px">YEVGEN DORLIN</div>
  <div class="frame name-box" style="left:626px;top:696px">GERALD MARWOOD</div>
  <div class="frame name-box" style="left:219px;top:760px">RONALD HAVERLY</div>
  <div class="frame name-box" style="left:496px;top:760px">ZSOLT VÁRADY</div>

  <h2 class="centered section-head" style="top:830px">ORGAN</h2>
  <div class="frame name-box" style="left:347px;top:873px">JULIET ANSLEY</div>

  <p class="centered director">ARTISTIC DIRECTOR <strong>ILONA KERTAVARI</strong></p>

  <span class="tickets-label">Tickets:</span>
  <span class="price" style="left:131px">$30</span>
  <span class="price" style="left:264px">$25</span>
  <span class="price" style="left:398px">$10</span>
  <div class="free-box">
    <p class="free-word">FREE</p>
    <p class="free-note">Students / Children under 12</p>
  </div>

  <p class="centered programmes">Programmes</p>
  <span class="donation-rule" style="left:147px"></span>
  <p class="centered donation">GOLD COIN DONATION</p>
  <span class="donation-rule" style="left:692px"></span>
</main>
</body>
</html>
```